Musician looking for catchy Web Design for promotion

My name is Brenna Colfer. I'm an Irish musician who plays the tin whistle and the flute. I'm also the leader of a traditional Irish music and dance ensemble called Wander the Hillside (www.wanderthehillside-example.com) and for the past 30 years, I've toured the world performing thousands of concerts. I run an annual cruise (www.brennacolfervoyage-example.com) that I would like a link to, and I'm also I'm organizing tours to Ireland that I would like a page set up for. I'm looking for a website to promote my tours and my music.
Updates

Hello Graphic Designers, I am only looking for the design of the home page to make my decision. Thank you. Brenna

Target Market(s)

Music fans of Irlsh and World Music

Industry/Entity Type

Entertainment Industry

Number of Pages Required

5+ page

Requirements
Must have
• I'm looking for a catchy design that shows a photo of me. I would like a few links....
• BIO
• TOURDATES
• BRENNA COLFER CRUISE
• MUSICAL TOUR OF IRELAND
• CONTACT
• VIDEO
• GALLERY
• CONTACT
• MAILING LIST
• STORE
Nice to have
• we'll see!

```html
<!DOCTYPE html>
<html lang="en">
<head>
<meta charset="utf-8">
<title>Brenna Colfer — Irish Musician</title>
<link href="https://fonts.googleapis.com/css2?family=Open+Sans:wght@400;600;700&family=Quicksand:wght@400;500;700&display=swap" rel="stylesheet">
<style>
:root{
  --gold:#c9a24b;
  --gold-deep:#a9822f;
  --gold-band:#b8923c;
  --ink:#1c1c1c;
  --ink-soft:#2a2a2a;
  --text:#555;
  --muted:#888;
  --paper:#ffffff;
  --grey-band:#ededed;
  --line:#dcdcdc;
}
*{box-sizing:border-box;margin:0;padding:0}
html,body{width:1200px;height:2408px;overflow:hidden}
body{font-family:"Open Sans",Arial,sans-serif;color:var(--text);background:var(--paper);font-size:14px}
.wrap{width:1000px;margin:0 auto;position:relative}

/* top bar */
.topbar{height:28px;background:var(--ink);color:#ddd;font-size:12px}
.topbar .wrap{display:flex;align-items:center;height:28px;gap:26px}
.topbar .item{display:flex;align-items:center;gap:6px}
.topbar .right{margin-left:auto;display:flex;align-items:center;gap:6px}
.dot{width:16px;height:16px;border-radius:50%;background:var(--gold)}
.search{width:90px;height:18px;background:#fff;border-radius:2px;margin-left:8px}

/* header */
.header{height:104px;background:var(--ink-soft)}
.header .wrap{display:flex;align-items:center;height:104px}
.brand{display:flex;align-items:center;gap:10px}
.brand .mark{width:40px;height:40px;border-radius:50%;background:var(--gold)}
.brand .name{font-family:"Quicksand",sans-serif;font-weight:700;color:#fff;font-size:20px;letter-spacing:1px}
.nav{margin-left:auto;display:flex;gap:22px}
.nav a{color:#fff;text-decoration:none;font-size:13px;font-weight:600}

/* hero */
.hero{height:508px;position:relative;background:linear-gradient(90deg,#5a2a16 0%,#8c4a22 35%,#c8a070 60%,#d9c9a8 80%,#8a6b46 100%)}
.hero .label{position:absolute;right:110px;color:#fff;font-family:"Quicksand",sans-serif;font-weight:700;font-size:20px;text-align:center}
.hero .label .ring{width:76px;height:76px;border-radius:50%;border:3px solid #fff;background:#b89565;margin:0 auto 6px}
.hero .caption{position:absolute;left:0;right:0;bottom:0;height:44px;background:rgba(0,0,0,.65);color:#fff;font-family:"Quicksand",sans-serif;font-size:24px;line-height:44px;padding-left:40px}
.hero .dots{position:absolute;bottom:56px;left:50%;transform:translateX(-50%);display:flex;gap:8px}
.hero .dots span{width:10px;height:10px;border-radius:50%;background:#fff;opacity:.6}
.hero .dots span.on{opacity:1;background:var(--gold)}

/* about */
.about{height:380px;text-align:center;padding-top:40px}
.sec-title{font-family:"Quicksand",sans-serif;font-weight:500;color:var(--gold);font-size:34px}
.rule{width:100%;height:1px;background:var(--line);margin:14px auto 18px}
.about p{font-size:13px;line-height:22px;width:1000px;margin:0 auto}
.more{display:inline-block;margin-top:22px;color:var(--ink);font-weight:600;font-size:13px}

/* tours */
.tours{height:360px;background:var(--gold-band);padding-top:22px}
.tours .head{display:flex;align-items:center;justify-content:space-between}
.tours .sec-title{color:#fff}
.arrows{display:flex;gap:6px}
.arrows svg{width:20px;height:20px}
.cards{display:flex;gap:18px;margin-top:22px}
.card{width:186px;background:#fff;padding:8px;height:240px}
.card .img{height:108px;background:linear-gradient(180deg,#8fc3e8,#e9eef2 60%,#3f6f92)}
.card h4{font-family:"Quicksand",sans-serif;color:var(--gold-deep);font-size:14px;margin-top:8px}
.card p{font-size:11px;line-height:15px;color:var(--muted);margin-top:4px}
.card .date{font-size:12px;font-weight:700;color:var(--ink);margin-top:6px}
.btn{display:inline-block;background:var(--gold);color:#fff;font-size:11px;font-weight:600;padding:4px 12px;margin-top:6px}

/* features */
.features{height:380px;padding-top:34px}
.features .cols{display:flex;gap:40px}
.feature{width:306px}
.feature h3{font-family:"Quicksand",sans-serif;font-weight:500;color:var(--gold);font-size:28px;margin-bottom:12px}
.feature .img{height:180px;position:relative}
.feature .img .tag{position:absolute;left:0;bottom:12px;background:var(--gold);color:#fff;font-weight:700;font-size:15px;padding:6px 14px}
.feature p{font-size:12px;line-height:18px;margin-top:12px}
.ship{background:linear-gradient(180deg,#a9cfe9,#f2f4f5 55%,#3c6d8e)}
.coast{background:linear-gradient(180deg,#7fb0d8,#cfd9df 45%,#6e6a5c 75%,#2f5572)}
.video{background:linear-gradient(180deg,#2b1b14,#7a3f26 60%,#111)}
.video .bar{position:absolute;left:0;right:0;bottom:0;height:20px;background:#111}

/* testimonials */
.testi{height:228px;background:var(--grey-band);padding-top:22px;text-align:center}
.testi .row{display:flex;align-items:center;gap:24px;margin-top:28px;text-align:left}
.quote{display:flex;gap:16px;flex:1}
.avatar{width:86px;height:86px;border-radius:50%;flex:none;background:radial-gradient(circle,#c9a785,#6b4a36)}
.quote p{font-size:12px;line-height:18px}
.quote .who{color:var(--gold-deep);font-weight:600;font-size:12px;margin-top:8px}

/* footer nav */
.fnav{height:42px;background:var(--ink);margin-top:10px}
.fnav .wrap{display:flex;gap:40px;align-items:center;height:42px}
.fnav a{color:#ddd;text-decoration:none;font-size:12px;font-weight:600}
.fnav a.on{color:var(--gold)}

/* footer */
.footer{height:330px;background:var(--ink-soft);color:#ccc;padding-top:20px}
.footer .cols{display:flex;gap:40px}
.footer h5{font-family:"Quicksand",sans-serif;font-weight:500;color:#fff;font-size:24px;margin-bottom:16px}
.fcol{width:306px;font-size:12px;line-height:20px}
.crow{display:flex;gap:10px;align-items:flex-start;margin-bottom:12px}
.crow svg{width:16px;height:16px;flex:none;margin-top:2px}
.field{height:28px;background:#fff;margin:12px 0 10px;padding-left:8px;color:#999;line-height:28px}
.gallery{display:grid;grid-template-columns:repeat(3,1fr);gap:8px}
.gallery div{height:70px;background:linear-gradient(135deg,#4a3a30,#8a6a4e)}
.copy{height:48px;background:#111;color:#aaa;font-size:12px;line-height:48px}
</style>
</head>
<body>

<div class="topbar">
  <div class="wrap">
    <div class="item"><svg width="12" height="12" viewBox="0 0 24 24"><path fill="#c9a24b" d="M6.6 10.8a15 15 0 006.6 6.6l2.2-2.2a1 1 0 011-.25 11 11 0 003.5.56 1 1 0 011 1V20a1 1 0 01-1 1A17 17 0 013 4a1 1 0 011-1h3.5a1 1 0 011 1 11 11 0 00.56 3.5 1 1 0 01-.25 1z"/></svg>052 555 0189</div>
    <div class="item"><svg width="12" height="12" viewBox="0 0 24 24"><rect x="2" y="5" width="20" height="14" fill="#c9a24b"/><path d="M2 5l10 8 10-8" stroke="#1c1c1c" stroke-width="2" fill="none"/></svg>info@brennacolfer-example.com</div>
    <div class="right"><span class="dot"></span><span class="dot"></span><span class="dot"></span><span class="dot"></span><span class="dot"></span><span class="search"></span></div>
  </div>
</div>

<header class="header">
  <div class="wrap">
    <div class="brand"><span class="mark"></span><span class="name">BRENNA COLFER</span></div>
    <nav class="nav">
      <a href="#">Bio</a><a href="#">Tour Dates</a><a href="#">Brenna Colfer Cruise</a><a href="#">Musical Tour Of Ireland</a><a href="#">Video</a><a href="#">Gallery</a><a href="#">Store</a><a href="#">Contact Us</a>
    </nav>
  </div>
</header>

<section class="hero" role="img" aria-label="Photo of Brenna Colfer with a row of tin whistles and flutes">
  <div class="label" style="top:150px"><div class="ring"></div>Tin Whistle</div>
  <div class="label" style="top:290px"><div class="ring"></div>The Flute</div>
  <div class="dots"><span class="on"></span><span></span><span></span></div>
  <div class="caption">I am Brenna Colfer I am an Irish musician who plays the tin whistle and the flute.</div>
</section>

<section class="about">
  <div class="wrap">
    <h2 class="sec-title">About Brenna Colfer's</h2>
    <div class="rule"></div>
    <p>Brenna Colfer has spent three decades carrying Irish music to stages across the world. A master of the tin whistle and the flute, she leads the ensemble Wander the Hillside and has played thousands of concerts on every continent. Her sound blends old tunes from the west of Ireland with a warm modern spirit, and every show feels like a kitchen session among friends. Join her at sea, travel with her through Ireland, or catch her next concert near you and hear why audiences keep coming back year after year.</p>
    <a class="more">Read More</a>
  </div>
</section>

<section class="tours">
  <div class="wrap">
    <div class="head">
      <h2 class="sec-title">Tour Dates</h2>
      <div class="arrows">
        <svg viewBox="0 0 20 20"><path d="M12 5l-5 5 5 5" stroke="#fff" stroke-width="2" fill="none"/></svg>
        <svg viewBox="0 0 20 20"><path d="M8 5l5 5-5 5" stroke="#fff" stroke-width="2" fill="none"/></svg>
      </div>
    </div>
    <div class="cards">
      <div class="card"><div class="img" role="img" aria-label="Cruise ship at sea"></div><h4>Caribbean Music Cruise</h4><p>Seven nights of tunes and dancing at sea.</p><div class="date">10 Feb 2016</div><span class="btn">Book Now</span></div>
      <div class="card"><div class="img" role="img" aria-label="Cruise ship in harbour"></div><h4>Galway Bay Session</h4><p>An evening of reels by the Atlantic shore.</p><div class="date">10 Feb 2016</div><span class="btn">Book Now</span></div>
      <div class="card"><div class="img" role="img" aria-label="Harbour city skyline"></div><h4>Dublin Concert Hall</h4><p>Brenna and the band live in the capital.</p><div class="date">10 Feb 2016</div><span class="btn">Book Now</span></div>
      <div class="card"><div class="img" role="img" aria-label="Cruise ship by a pier"></div><h4>Boston Irish Festival</h4><p>A weekend of music, song and céilí dance.</p><div class="date">10 Feb 2016</div><span class="btn">Book Now</span></div>
      <div class="card"><div class="img" role="img" aria-label="Ship deck with swimming pool"></div><h4>Atlantic Crossing Gala</h4><p>A special night of whistles and flutes.</p><div class="date">10 Feb 2016</div><span class="btn">Book Now</span></div>
    </div>
  </div>
</section>

<section class="features">
  <div class="wrap cols">
    <div class="feature"><h3>Brenna Colfer's cruise</h3><div class="img ship" role="img" aria-label="Large cruise ship on open water"><span class="tag">Book Now</span></div><p>Sail with Brenna and friends for a week of music, dance and song at sea.</p></div>
    <div class="feature"><h3>Musical Tour of Ireland</h3><div class="img coast" role="img" aria-label="Irish coastline with a lighthouse"><span class="tag">Book Now</span></div><p>Travel the west of Ireland with nightly sessions in the finest local pubs.</p></div>
    <div class="feature"><h3>View Our Video</h3><div class="img video" role="img" aria-label="Video still of the ensemble on stage"><div class="bar"></div></div><p>Watch Brenna and Wander the Hillside perform live on their latest world tour.</p></div>
  </div>
</section>

<section class="testi">
  <div class="wrap">
    <h2 class="sec-title">Client Testimonials</h2>
    <div class="row">
      <svg width="20" height="20" viewBox="0 0 20 20"><path d="M12 5l-5 5 5 5" stroke="#999" stroke-width="2" fill="none"/></svg>
      <div class="quote"><div class="avatar" role="img" aria-label="Portrait of a concert guest"></div><div><p>The cruise was the best week of our year. Brenna's playing filled the ship with joy and we made friends from all over the world.</p><div class="who">Maura Quinlan</div></div></div>
      <div class="quote"><div class="avatar" role="img" aria-label="Portrait of a tour guest"></div><div><p>Touring Ireland with live music every night was a dream. Every detail was cared for and the sessions were simply unforgettable.</p><div class="who">Declan Foyle</div></div></div>
      <svg width="20" height="20" viewBox="0 0 20 20"><path d="M8 5l5 5-5 5" stroke="#999" stroke-width="2" fill="none"/></svg>
    </div>
  </div>
</section>

<nav class="fnav">
  <div class="wrap">
    <a class="on" href="#">HOME</a><a href="#">BIO</a><a href="#">TOUR DATES</a><a href="#">BRENNA COLFER CRUISE</a><a href="#">MUSICAL TOUR OF IRELAND</a><a href="#">VIDEO</a><a href="#">GALLERY</a><a href="#">STORE</a><a href="#">CONTACT US</a>
  </div>
</nav>

<footer class="footer">
  <div class="wrap cols">
    <div class="fcol">
      <h5>Contact Details</h5>
      <div class="crow"><svg viewBox="0 0 24 24"><path fill="#c9a24b" d="M12 2a7 7 0 00-7 7c0 5 7 13 7 13s7-8 7-13a7 7 0 00-7-7zm0 9.5A2.5 2.5 0 1112 6a2.5 2.5 0 010 5.5z"/></svg><span>Brenna Colfer<br>12 Harbour Road, Doolin, Co. Clare</span></div>
      <div class="crow"><svg viewBox="0 0 24 24"><path fill="#c9a24b" d="M6.6 10.8a15 15 0 006.6 6.6l2.2-2.2a1 1 0 011-.25 11 11 0 003.5.56 1 1 0 011 1V20a1 1 0 01-1 1A17 17 0 013 4a1 1 0 011-1h3.5a1 1 0 011 1 11 11 0 00.56 3.5 1 1 0 01-.25 1z"/></svg><span>052 555 0189</span></div>
      <div class="crow"><svg viewBox="0 0 24 24"><rect x="2" y="5" width="20" height="14" fill="#c9a24b"/><path d="M2 5l10 8 10-8" stroke="#2a2a2a" stroke-width="2" fill="none"/></svg><span>info@brennacolfer-example.com</span></div>
    </div>
    <div class="fcol">
      <h5>Newsletter Sign Up</h5>
      <p>Get tour news and new releases straight to your inbox.</p>
      <div class="field">Email Address</div>
      <span class="btn">SUBSCRIBE</span>
    </div>
    <div class="fcol">
      <h5>Photo Gallery</h5>
      <div class="gallery" role="img" aria-label="Grid of concert and tour photos">
        <div></div><div></div><div></div><div></div><div></div><div></div>
      </div>
    </div>
  </div>
</footer>

<div class="copy"><div class="wrap">Copyright © 2016 Brenna Colfer's Musical Tour Of Ireland. All Rights Reserved.</div></div>

</body>
</html>
```